KRT business cards

I need a Business card design for my self. I am behavior analyst owner of a new company based in Miami. We offer Applied Behavior Analysis (ABA) services to individuals with developmental disabilities.

Business

```html
<!DOCTYPE html>
<html lang="en">
<head>
<meta charset="utf-8">
<title>KRT Business Cards</title>
<link href="https://fonts.googleapis.com/css2?family=Lato:wght@400;700;900&display=swap" rel="stylesheet">
<style>
  :root {
    --navy: #1c4680;
    --navy-deep: #163a6c;
    --leaf: #4a9e3d;
    --paper: #ffffff;
    --ink-soft: #4a9e3d;
    --backdrop: #ece8e2;
  }
  * { box-sizing: border-box; margin: 0; padding: 0; }
  html, body {
    width: 1200px; height: 1000px; overflow: hidden;
    background: var(--backdrop);
    font-family: "Lato", Arial, sans-serif;
  }
  .sheet {
    width: 1200px; height: 1000px;
    display: flex; flex-direction: column; align-items: center; justify-content: center;
    gap: 60px;
  }
  .card {
    width: 700px; height: 400px;
    box-shadow: 0 6px 18px rgba(0,0,0,0.18);
    position: relative; overflow: hidden;
  }
  /* Front */
  .card-front {
    background: var(--navy);
    display: flex; flex-direction: column; align-items: center; justify-content: center;
    gap: 18px;
  }
  .brand-mark {
    width: 120px; height: 120px; border-radius: 50%;
    background: var(--leaf);
  }
  .brand-name {
    color: var(--paper);
    font-weight: 700; font-size: 40px; letter-spacing: 3px;
    text-transform: uppercase;
  }
  /* Back */
  .card-back {
    background: var(--paper);
    display: flex;
  }
  .back-emblem {
    width: 330px; height: 100%;
    display: flex; align-items: center; justify-content: center;
  }
  .back-emblem .brand-mark { width: 230px; height: 230px; }
  .details {
    flex: 1; padding: 52px 0 0 20px;
  }
  .person-name {
    color: var(--navy); font-weight: 900; font-size: 25px; letter-spacing: 0.5px;
  }
  .person-role {
    color: var(--leaf); font-size: 19px; margin-top: 2px;
  }
  .rule {
    height: 3px; background: var(--leaf); margin: 12px 0 28px; width: 100%;
  }
  .contact-list { list-style: none; color: var(--navy); font-size: 17px; line-height: 1.45; }
  .contact-list span.label { display: inline-block; width: 34px; }
  .company {
    margin-top: 30px; color: var(--navy); font-weight: 900; font-size: 17px;
  }
  .address { color: var(--leaf); font-size: 17px; line-height: 1.35; margin-top: 2px; }
  .web { margin-top: 26px; font-weight: 700; font-size: 17px; color: var(--navy); }
  .web .accent { color: var(--leaf); }
</style>
</head>
<body>
<main class="sheet">
  <section class="card card-front">
    <div class="brand-mark" aria-hidden="true"></div>
    <div class="brand-name">Kindred Roots Therapy</div>
  </section>

  <section class="card card-back">
    <div class="back-emblem">
      <div class="brand-mark" aria-hidden="true"></div>
    </div>
    <div class="details">
      <div class="person-name">ALEX MORENO</div>
      <div class="person-role">Director</div>
      <div class="rule"></div>
      <ul class="contact-list">
        <li><span class="label">T</span>305 555 014 218</li>
        <li><span class="label">M</span>305 555 027 364</li>
        <li><span class="label">F</span>305 555 039 710</li>
      </ul>
      <div class="company">KINDRED ROOTS THERAPY</div>
      <div class="address">Street 8, Suite 2 Coral Way,<br>Miami, Florida, US 33145</div>
      <div class="web">www.kindredroots<span class="accent">therapy</span>.com</div>
    </div>
  </section>
</main>
</body>
</html>
```